Company letterhead, compliments slip and business card design for Electrical Contracting Company
Colm Dwyer Electrical
Corporate
Declan Dwyer
Managing DIrector
Cloon
Mullan Road
Dundalk
Louth
declan@colmdwyer.com
www.colmdwyer.com

```html
<!DOCTYPE html>
<html lang="en">
<head>
<meta charset="utf-8">
<title>Colm Dwyer Electrical — Stationery</title>
<link href="https://fonts.googleapis.com/css2?family=Open+Sans:wght@400;600;700&family=Pinyon+Script&display=swap" rel="stylesheet">
<style>
  :root{
    --bg:#e4e4e6;
    --paper:#ffffff;
    --red:#d7262c;
    --dark:#3a3a3c;
    --grey:#9a9a9d;
    --band:#c9c9cc;
    --card-grey:#8e8e91;
    --text:#4a4a4d;
    --badge-blue:#2c6fb6;
    --badge-green:#7bbf3a;
  }
  *{box-sizing:border-box;margin:0;padding:0}
  html,body{width:1200px;height:799px;overflow:hidden}
  body{background:var(--bg);font-family:"Open Sans",Arial,sans-serif;color:var(--text);position:relative}
  .sheet{position:absolute;background:var(--paper);box-shadow:0 4px 14px rgba(0,0,0,.18);overflow:hidden}

  .brand{display:flex;align-items:center;gap:7px}
  .brand-mark{width:14px;height:14px;background:var(--red);flex:none}
  .brand-name{font-weight:700;color:var(--dark);font-size:14px;letter-spacing:.3px;text-transform:uppercase;white-space:nowrap}
  .brand-tag{font-size:7px;color:var(--red);letter-spacing:1.6px;text-transform:uppercase;margin-top:3px;padding-left:21px;white-space:nowrap}

  .contact-list{list-style:none;font-size:8px;line-height:1.55;color:var(--text)}
  .contact-list li{display:flex;align-items:center;gap:5px;white-space:nowrap}
  .icon{width:7px;height:7px;flex:none}

  .band{position:absolute;left:0;right:0;bottom:0;height:22px;background:var(--band)}
  .band-accent{position:absolute;left:0;bottom:0;height:100%;background:var(--red);clip-path:polygon(0 0,86% 0,100% 100%,0 100%)}
  .band-web{position:absolute;bottom:50%;transform:translateY(50%);font-size:8px;letter-spacing:2px;color:#fff}

  /* Letterhead */
  .letterhead{left:40px;top:60px;width:480px;height:679px}
  .letterhead .brand-block{position:absolute;left:34px;top:40px}
  .letterhead .header-contact{position:absolute;right:34px;top:40px;display:flex;gap:16px;align-items:flex-start}
  .letterhead .address{font-size:8px;line-height:1.55;color:var(--text)}
  .letterhead .badges{position:absolute;left:34px;bottom:44px;display:flex;gap:12px;align-items:center}
  .badge{width:38px;height:38px}
  .badge.square{background:var(--badge-blue);border-radius:3px}
  .badge.circle{border-radius:50%;border:3px solid var(--badge-blue);background:#fff}
  .badge.circle.green{border-color:var(--badge-green)}
  .letterhead .legal{position:absolute;right:34px;bottom:46px;width:230px;font-size:6.5px;line-height:1.5;text-align:right;color:var(--grey)}
  .letterhead .band-accent{width:120px}
  .letterhead .band-web{left:200px}

  /* Compliments slip */
  .comp-slip{left:560px;top:60px;width:600px;height:283px}
  .comp-slip .brand-block{position:absolute;left:34px;top:40px}
  .comp-slip .compliments{position:absolute;right:40px;top:168px;font-family:"Pinyon Script",cursive;font-size:30px;color:var(--dark);white-space:nowrap}
  .comp-slip .band{height:26px}
  .comp-slip .band-accent{width:150px}
  .comp-slip .band-web{left:190px}

  /* Business cards */
  .card{top:400px;width:290px;height:188px}
  .card-back{left:560px;background:var(--card-grey)}
  .card-back .brand{position:absolute;left:50%;top:50%;transform:translate(-50%,-50%)}
  .card-back .brand-name{color:#fff;font-size:12px}
  .card-back .brand-mark{width:12px;height:12px}
  .card-front{left:870px}
  .card-front .brand-block{position:absolute;left:16px;top:118px}
  .card-front .brand-name{font-size:10px}
  .card-front .brand-mark{width:11px;height:11px}
  .card-front .brand-tag{font-size:5.5px;padding-left:18px;letter-spacing:1.2px}
  .card-front .person{position:absolute;right:16px;top:16px;width:128px}
  .person-name{font-size:10px;font-weight:700;color:var(--dark)}
  .person-role{font-size:7px;color:var(--grey);margin-bottom:6px}
  .card-front .contact-list{font-size:6.5px}
  .card-front .band{height:16px}
  .card-front .band-accent{width:80px}
</style>
</head>
<body>

<svg width="0" height="0" style="position:absolute">
  <defs>
    <symbol id="icon-phone" viewBox="0 0 10 10"><path d="M2 1h2l1 2.5-1.3.8a5.5 5.5 0 0 0 2 2l.8-1.3L9 6v2a1 1 0 0 1-1 1A7 7 0 0 1 1 2a1 1 0 0 1 1-1z" fill="#d7262c"/></symbol>
    <symbol id="icon-mail" viewBox="0 0 10 10"><rect x="0.5" y="2" width="9" height="6" fill="#d7262c"/><path d="M0.5 2 5 5.5 9.5 2" stroke="#fff" stroke-width="0.8" fill="none"/></symbol>
    <symbol id="icon-pin" viewBox="0 0 10 10"><path d="M5 0.5a3.3 3.3 0 0 1 3.3 3.3C8.3 6.3 5 9.5 5 9.5S1.7 6.3 1.7 3.8A3.3 3.3 0 0 1 5 .5z" fill="#d7262c"/><circle cx="5" cy="3.8" r="1.1" fill="#fff"/></symbol>
  </defs>
</svg>

<section class="sheet letterhead">
  <div class="brand-block">
    <div class="brand"><span class="brand-mark"></span><span class="brand-name">Colm Dwyer Electrical</span></div>
    <div class="brand-tag">Domestic · Commercial · Industrial</div>
  </div>
  <div class="header-contact">
    <p class="address">Cloon<br>Mullan Road<br>Dundalk<br>Co. Louth</p>
    <ul class="contact-list">
      <li><svg class="icon"><use href="#icon-phone"/></svg>+353 42 555 0190</li>
      <li><svg class="icon"><use href="#icon-phone"/></svg>+353 86 555 0142</li>
      <li><svg class="icon"><use href="#icon-mail"/></svg>declan@colmdwyer.com</li>
    </ul>
  </div>
  <div class="badges">
    <div class="badge square" role="img" aria-label="Certification badge"></div>
    <div class="badge circle" role="img" aria-label="Association badge"></div>
    <div class="badge circle green" role="img" aria-label="Accreditation badge"></div>
  </div>
  <p class="legal">Colm Dwyer Electrical Ltd. Registered in Ireland. Company No. 555019. VAT No. IE5550190X.</p>
  <div class="band"><div class="band-accent"></div><span class="band-web">www.colmdwyer.com</span></div>
</section>

<section class="sheet comp-slip">
  <div class="brand-block">
    <div class="brand"><span class="brand-mark"></span><span class="brand-name">Colm Dwyer Electrical</span></div>
    <div class="brand-tag">Domestic · Commercial · Industrial</div>
  </div>
  <p class="compliments">With Compliments</p>
  <div class="band"><div class="band-accent"></div><span class="band-web">www.colmdwyer.com</span></div>
</section>

<section class="sheet card card-back">
  <div class="brand"><span class="brand-mark"></span><span class="brand-name">Colm Dwyer Electrical</span></div>
</section>

<section class="sheet card card-front">
  <div class="person">
    <p class="person-name">Declan Dwyer</p>
    <p class="person-role">Managing Director</p>
    <ul class="contact-list">
      <li><svg class="icon"><use href="#icon-phone"/></svg>+353 86 555 0142</li>
      <li><svg class="icon"><use href="#icon-phone"/></svg>+353 42 555 0190</li>
      <li><svg class="icon"><use href="#icon-mail"/></svg>declan@colmdwyer.com</li>
      <li><svg class="icon"><use href="#icon-pin"/></svg>Cloon, Mullan Road, Dundalk</li>
    </ul>
  </div>
  <div class="brand-block">
    <div class="brand"><span class="brand-mark"></span><span class="brand-name">Colm Dwyer Electrical</span></div>
    <div class="brand-tag">Domestic · Commercial · Industrial</div>
  </div>
  <div class="band"><div class="band-accent"></div></div>
</section>

</body>
</html>
```